Business card design for Automotive workshop

We need a business card for a new automotive repair and tyre shop called Ridgeback Prime Automotive located in New Zealand. We are a clean, modern and fresh workshop and company.

Front needs to feature logo,
my name:
Lachie Westergaard (director)

Address:
48 Marlow Lane
Kaiwera Bay 3582

Phone: 07 842 1937
Mobile: 027 519 2764
Email: office@ridgebackmotors.co.nz
Website: ridgebackmotors.co.nz

Back needs to feature an area to write down appointment details, date and time.

Also feature a list of jobs and work we do such as,
Vehicle Servicing
All Mechanical Repairs
Warrant of Fitness
Tyres & Wheel Alignments
Automotive Diagnostics
Automotive Parts & Supplies

```html
<!DOCTYPE html>
<html lang="en">
<head>
<meta charset="utf-8">
<title>Ridgeback Prime Automotive – Business Card</title>
<link rel="stylesheet" href="https://fonts.googleapis.com/css2?family=Roboto:wght@400;700&family=Roboto+Condensed:wght@700&display=swap">
<style>
  :root {
    --ink: #0e0e10;
    --red: #c41e35;
    --white: #ffffff;
    --track: #c9c8ca;
    --page: #f2f2f4;
  }
  * { box-sizing: border-box; margin: 0; padding: 0; }
  html, body { width: 1200px; height: 1000px; overflow: hidden; }
  body {
    background: var(--page);
    font-family: "Roboto", Arial, sans-serif;
    position: relative;
  }
  .card {
    position: absolute;
    width: 620px;
    height: 345px;
    border-radius: 48px;
    overflow: hidden;
  }
  /* Front */
  .card-front { left: 70px; top: 120px; background: var(--ink); color: var(--white); }
  .brand {
    position: absolute; left: 0; right: 0; top: 66px;
    text-align: center;
    font-weight: 700; font-size: 30px; letter-spacing: 1px;
    text-transform: uppercase; color: var(--red);
  }
  .brand-underline {
    position: absolute; left: 72px; right: 72px; top: 118px;
    height: 2px; background: var(--white);
  }
  .person {
    position: absolute; right: 375px; top: 182px; text-align: right;
  }
  .person-name {
    font-family: "Roboto Condensed", Arial, sans-serif;
    font-weight: 700; font-size: 24px; color: var(--red); letter-spacing: -0.3px;
  }
  .person-role { font-size: 15px; margin-top: 4px; }
  .address {
    position: absolute; right: 375px; top: 255px; text-align: right;
    font-size: 18px; line-height: 22px; white-space: nowrap;
  }
  .address svg { vertical-align: -3px; margin-right: 6px; }
  .divider {
    position: absolute; left: 261px; top: 173px; width: 2px; height: 140px;
    background: var(--white);
  }
  .contacts { position: absolute; left: 273px; top: 182px; list-style: none; }
  .contacts li {
    display: flex; align-items: center; gap: 10px;
    font-size: 18px; height: 31px;
  }
  .contacts svg { width: 22px; height: 22px; flex: none; }
  /* Back */
  .card-back { left: 510px; top: 535px; background: var(--white); }
  .tracks { position: absolute; inset: 0; }
  .booking {
    position: absolute; left: 66px; top: 68px; width: 456px;
    list-style: none; color: var(--red);
    font-family: "Roboto Condensed", Arial, sans-serif; font-weight: 700; font-size: 20px;
  }
  .booking li { display: flex; align-items: baseline; height: 22px; }
  .booking .fill {
    flex: 1; margin-left: 6px;
    border-bottom: 3px dotted var(--red); transform: translateY(-3px);
  }
  .services {
    position: absolute; right: 100px; top: 168px;
    list-style: none; text-align: right;
    color: var(--red); font-size: 19px; line-height: 22px;
  }
</style>
</head>
<body>

<section class="card card-front" aria-label="Card front">
  <div class="brand">Ridgeback Prime Automotive</div>
  <div class="brand-underline"></div>

  <div class="person">
    <div class="person-name">Lachie Westergaard</div>
    <div class="person-role">DIRECTOR</div>
  </div>
  <div class="address">
    48 Marlow Lane<br>
    <svg width="16" height="20" viewBox="0 0 16 20" aria-hidden="true"><path d="M8 1a6.5 6.5 0 0 0-6.5 6.5C1.5 12 8 19 8 19s6.5-7 6.5-11.5A6.5 6.5 0 0 0 8 1z" fill="none" stroke="#c41e35" stroke-width="1.6"/><circle cx="8" cy="7.5" r="2.3" fill="none" stroke="#c41e35" stroke-width="1.6"/></svg>Kaiwera Bay 3582
  </div>

  <div class="divider"></div>

  <ul class="contacts">
    <li><svg viewBox="0 0 24 24" aria-hidden="true"><path d="M6 3l3 4-2 2c1 3 4 6 7 7l2-2 4 3-2 3C10 20 4 14 3 5z" fill="#c41e35"/></svg>07 842 1937</li>
    <li><svg viewBox="0 0 24 24" aria-hidden="true"><circle cx="12" cy="12" r="9.5" fill="none" stroke="#c41e35" stroke-width="1.6"/><path d="M8.5 7.5l2 2.5-1 1c.7 1.6 1.9 2.8 3.5 3.5l1-1 2.5 2-1.3 1.5C11.5 16.5 7.5 12.5 7 8.8z" fill="#c41e35"/></svg>027 519 2764</li>
    <li><svg viewBox="0 0 24 24" aria-hidden="true"><rect x="2.5" y="5" width="19" height="14" fill="none" stroke="#c41e35" stroke-width="1.6"/><path d="M2.5 5l9.5 8 9.5-8M2.5 19l7-6.5M21.5 19l-7-6.5" fill="none" stroke="#c41e35" stroke-width="1.6"/></svg>office@ridgebackmotors.co.nz</li>
    <li><svg viewBox="0 0 24 24" aria-hidden="true"><circle cx="12" cy="12" r="9.5" fill="none" stroke="#c41e35" stroke-width="1.6"/><ellipse cx="12" cy="12" rx="4" ry="9.5" fill="none" stroke="#c41e35" stroke-width="1.6"/><path d="M2.5 12h19M12 2.5v19" stroke="#c41e35" stroke-width="1.6"/></svg>ridgebackmotors.co.nz</li>
  </ul>
</section>

<section class="card card-back" aria-label="Card back">
  <svg class="tracks" viewBox="0 0 620 345" role="img" aria-label="Grey tyre tread tracks running diagonally across the lower left">
    <polygon points="0,20 40,0 360,345 290,345 0,70" fill="var(--track)"/>
    <polygon points="0,185 0,225 112,345 155,345" fill="var(--track)"/>
    <polygon points="0,235 0,260 80,345 100,345" fill="var(--track)"/>
  </svg>

  <ul class="booking">
    <li>Details:<span class="fill"></span></li>
    <li>Date:<span class="fill"></span></li>
    <li>Time:<span class="fill"></span></li>
  </ul>

  <ul class="services">
    <li>Vehicle Servicing</li>
    <li>All Mechanical Repairs</li>
    <li>Warrant of Fitness</li>
    <li>Tyres &amp; Wheel Alignments</li>
    <li>Automotive Diagnostics</li>
    <li>Automotive Parts &amp; Supplies</li>
  </ul>
</section>

</body>
</html>
```